Flyer Design Project

To whom it may concern
Would love the benefit of your expertise

I have a project which is to increase business activity. There are dozens or real estate adds and I want mine to stand out from all others.

My strategy is going with a 50 % sale, what I need is something catchy and something that will make my brochure stand out from the other dozen brochure they have in the mail I need the WOW! Factor

DL Brochure (DL Brochures, Size 99 mm X 210 mm) atm the moment im thinking of only using 1 side but if your design needs both side that is an option

below will be the wording I'm thinking of going with the describe the sale and benefits, i am flexible with the wording if your think something else will sound better

***New Wording***

50% OFF COMMISSION
Sounds good doesn’t it?
Our promise to you from Harlow Real Estate

List your property with us
And if your buyer has not been found within 15 days
We will slash 50% off our commission!
You will have the benefit of Real Estate consultants
Derek Harlow and Thomas Vellani
With over 40 years combined experience
Working hard to find your buyer.

Call Today 0471 829 156

Condition Apply

Follow us on Facebook www.facebook.com/quillbayhomes

I have attached the link to our website and Facebook page if you want to see a possible color scheme
but i am open to anything

http://brightkeysquillbay.com.au/
http://www.facebook.com/quillbayhomes

Good Luck !!!

Target Market(s)

Home Seller's

Industry/Entity Type

Real Estate

Requirements
Nice to have
• our logo but remember this flyer is not to market our self its to market our offer
so i want to 50% off the stand out not Brightkeys Harlow Real Estate
Should not have
• House in the Background, i would much rather the 50% take up half the page than have the house or even a quirky un related image

```html
<!DOCTYPE html>
<html lang="en">
<head>
<meta charset="utf-8">
<title>50% Off Commission – Harlow Real Estate</title>
<link rel="stylesheet" href="https://fonts.googleapis.com/css2?family=Oswald:wght@300;400;500&display=swap">
<style>
  :root {
    --red: #e0282e;
    --ink: #3b3d40;
    --paper: #ffffff;
    --stage: #ffffff;
    --hero-light: #f2f2f2;
    --hero-mid: #9a9b9d;
    --hero-dark: #4a4b4d;
  }
  * { margin: 0; padding: 0; box-sizing: border-box; }
  html, body {
    width: 670px;
    height: 1200px;
    overflow: hidden;
    background: var(--stage);
  }
  .flyer {
    position: relative;
    width: 670px;
    height: 1200px;
    background: var(--paper);
    font-family: "Oswald", "Arial Narrow", sans-serif;
    color: var(--ink);
    text-align: center;
    text-transform: uppercase;
    display: flex;
    flex-direction: column;
  }
  .hero-image {
    height: 450px;
    background:
      radial-gradient(circle at 62% 44%, rgba(224,40,46,0.55) 0 40px, transparent 70px),
      linear-gradient(160deg, var(--hero-dark) 0%, var(--hero-mid) 45%, var(--hero-light) 85%, var(--paper) 100%);
  }
  .headline {
    margin-top: 70px;
    line-height: 0.95;
    font-weight: 400;
  }
  .headline-offer {
    font-size: 150px;
    letter-spacing: 1px;
  }
  .headline-offer .percent { color: var(--red); }
  .headline-word {
    font-size: 104px;
    letter-spacing: 1px;
    margin-top: 4px;
  }
  .promise {
    margin-top: 28px;
    font-size: 31px;
    font-weight: 400;
    line-height: 1.15;
  }
  .promise .agency {
    display: block;
    color: var(--red);
    font-size: 40px;
    font-weight: 500;
    line-height: 1.15;
  }
  .details {
    margin-top: 6px;
    font-size: 24px;
    font-weight: 300;
    line-height: 1.32;
    text-transform: none;
  }
  .call-band {
    margin-top: auto;
    height: 118px;
    background: var(--red);
    color: var(--paper);
    display: flex;
    align-items: center;
    justify-content: center;
    font-size: 46px;
    font-weight: 400;
    letter-spacing: 1px;
  }
</style>
</head>
<body>
  <main class="flyer">
    <div class="hero-image" role="img" aria-label="Rows of small grey model houses with one red house picked out under a red magnifying glass"></div>

    <h1 class="headline">
      <span class="headline-offer"><span class="percent">50%</span> OFF</span><br>
      <span class="headline-word">COMMISSION</span>
    </h1>

    <p class="promise">
      Sounds good doesn’t it?<br>
      Our promise to you from
      <span class="agency">Harlow Real Estate</span>
    </p>

    <p class="details">
      List your property with us<br>
      And if your buyer has not been found within 15 days<br>
      We will slash 50% off our commission!<br>
      You will have the benefit of Real Estate consultants<br>
      Derek Harlow and Thomas Vellani<br>
      With over 40 years combined experience<br>
      Working hard to find your buyer.
    </p>

    <div class="call-band">Call today 0471 829 156</div>
  </main>
</body>
</html>
```